PowerPoint Design for KELPO Polls

KELPO Polls stands for 'Kindred Estimates Linking Population Outlooks Polls'. It is a collaborative research effort to format and combine multiple sources of public opinion data from around the world into merged datasets. We need a Microsoft PowerPoint design for our conference/workshop presentations and instructional videos used as part of our research efforts and crowdsourced development. The design should match the website design and logo, which are attached to this contest (these are the files from previous successful design contests).

Slides will contain a lot of data visualizations, tables with statistical output (lots of numbers), and figures. Bullet points will be used frequently on slides and larg blocks of text should be avided. Margins should be narrow to maximize space used and the size of fonts must be large enough (24-32+) to be visible at the back of classrooms and conference rooms.

I was away at a conference and am now busy with teaching preparation, so I need a few extra days to give adequate feedback.

Target Market(s)

academia, government, non-profits, postgraduates, researchers

Font styles to use
Sans Serif

Colors

Designer to choose colors to be used in the design.

Requirements
Must have
• designs for common slide layouts
Nice to have
• thematic link with website design and logo

```html
<!DOCTYPE html>
<html lang="en">
<head>
<meta charset="utf-8">
<title>KELPO Polls – Slide Designs</title>
<link rel="stylesheet" href="https://fonts.googleapis.com/css2?family=Catamaran:wght@800&family=Roboto:wght@300;400;700&display=swap">
<style>
  :root {
    --title-blue: #0b5cb3;
    --accent-blue: #1b9ad8;
    --body-text: #2f2f2f;
    --bracket-grey: #a9adb0;
    --page-grey: #9a9a9a;
    --canvas-bg: #ffffff;
  }
  * { box-sizing: border-box; margin: 0; padding: 0; }
  html, body {
    width: 1125px; height: 1200px; overflow: hidden;
    background: var(--canvas-bg);
  }
  .canvas { position: relative; width: 1125px; height: 1200px; }
  .slide {
    position: absolute; left: 81px; width: 962px; height: 541px;
    background: #fff;
    box-shadow: 3px 4px 5px rgba(0,0,0,0.55), 0 0 2px rgba(0,0,0,0.12);
    font-family: "Roboto", sans-serif; font-weight: 300; color: var(--body-text);
  }
  .slide--detail { top: 46px; }
  .slide--plain { top: 614px; }
  .bracket { position: absolute; top: 15px; width: 46px; height: 44px; border-top: 5px solid var(--bracket-grey); }
  .bracket--left { left: 20px; border-left: 5px solid var(--bracket-grey); }
  .bracket--right { left: 895px; border-right: 5px solid var(--bracket-grey); }
  .slide-title {
    position: absolute; left: 0; right: 0; top: 40px; text-align: center;
    font-family: "Catamaran", sans-serif; font-weight: 800; font-size: 50px;
    line-height: 1; letter-spacing: 0; white-space: nowrap; color: var(--title-blue);
  }
  .point, .subpoint { position: absolute; white-space: nowrap; line-height: 1; }
  .point::before, .subpoint::before { position: absolute; color: var(--accent-blue); }
  .point::before {
    content: ""; left: -29px; width: 11px; height: 11px; border: 1.6px solid var(--accent-blue); border-radius: 50%;
  }
  .subpoint::before {
    content: ""; left: -33px; width: 6px; height: 6px; background: var(--accent-blue); border-radius: 50%;
  }
  .slide--detail .point { left: 64px; font-size: 22.5px; transform: translateY(-50%); }
  .slide--detail .point::before { top: 7px; }
  .slide--detail .subpoint { left: 136px; font-size: 19px; transform: translateY(-50%); }
  .slide--detail .subpoint::before { top: 7px; }
  .slide--plain .point { left: 64px; font-size: 27.5px; transform: translateY(-50%); }
  .slide--plain .point::before { top: 10px; }
  .slide--plain .point--wrap { white-space: normal; width: 840px; line-height: 33px; transform: none; }
  .slide--plain .point--wrap::before { top: 13px; }
  .slide--plain .subpoint { left: 136px; font-size: 23.5px; transform: translateY(-50%); }
  .slide--plain .subpoint::before { top: 9px; }
  .hl { color: var(--accent-blue); font-weight: 400; }
  .hl-strong { color: var(--accent-blue); font-weight: 700; }
  .brand {
    position: absolute; left: 20px; top: 494px; display: flex; align-items: center; gap: 12px;
    font-family: "Roboto", sans-serif; font-weight: 700; font-size: 24px; color: var(--title-blue);
  }
  .brand-dot { width: 30px; height: 30px; border-radius: 50%; background: var(--accent-blue); }
  .page-number { position: absolute; left: 928px; top: 506px; font-size: 11px; color: var(--page-grey); font-weight: 400; }
</style>
</head>
<body>
<main class="canvas">
  <section class="slide slide--detail">
    <span class="bracket bracket--left"></span>
    <span class="bracket bracket--right"></span>
    <h1 class="slide-title">PERCEIVED ELECTORAL INTEGRITY</h1>
    <p class="point" style="top:149px">Refers to how fair or <span class="hl-strong">trustworthy</span> people think elections are</p>
    <p class="point" style="top:196px">Used as <span class="hl-strong">dependent variable</span> in this study</p>
    <p class="point" style="top:242px">Constructed from public survey questions that ask about:</p>
    <p class="subpoint" style="top:275px"><span class="hl">Honesty</span> of elections</p>
    <p class="subpoint" style="top:306px"><span class="hl">Fairness</span> of electoral process</p>
    <p class="subpoint" style="top:336px"><span class="hl">Trust</span> in elections</p>
    <p class="subpoint" style="top:366px"><span class="hl">Fairness</span> of elections</p>
    <p class="point" style="top:411px">Surveys use random sampling to be as nationally <span class="hl-strong">representative</span> as possible</p>
    <div class="brand"><span class="brand-dot"></span>KELPO Polls</div>
    <span class="page-number">3</span>
  </section>

  <section class="slide slide--plain">
    <span class="bracket bracket--left"></span>
    <span class="bracket bracket--right"></span>
    <h1 class="slide-title">PERCEIVED ELECTORAL INTEGRITY</h1>
    <p class="point" style="top:150px">Refers to how fair or trustworthy people think elections are</p>
    <p class="point" style="top:191px">Used as dependent variable in this study</p>
    <p class="point" style="top:232px">Constructed from public survey questions that ask about:</p>
    <p class="subpoint" style="top:268px">Honesty of elections</p>
    <p class="subpoint" style="top:303px">Fairness of electoral process</p>
    <p class="subpoint" style="top:338px">Trust in elections</p>
    <p class="subpoint" style="top:373px">Fairness of elections</p>
    <p class="point point--wrap" style="top:394px">Surveys use random sampling to be as nationally representative as possible</p>
    <div class="brand"><span class="brand-dot"></span>KELPO Polls</div>
    <span class="page-number">2</span>
  </section>
</main>
</body>
</html>
```